Entertainment Brochure Needed

The design needs to include information related to apartment designs.

Brochure Design Brief:
We are requiring an 8 ½” x 11 tri-fold brochure for marketing purposes for our entertainment company to distribute to our current and potential customers. The brochure exhibits services offered by our company along with themed events (DJ Services, Karaoke, Movie Night, Casino Night), Photo Booth, and concession machines/stations (Slushy Machines, Popcorn Machines, and Cotton Candy Machines). We require photos to depict our various themed events, along with the services we offer. We require the center (inside) of the brochure to flow through the brochure. We are looking to produce eye-catching graphics and content for all the services we offer.
As well as good marketing techniques.
Company Colors:
Maroon ( same color as the logo)
White
Black
It's okay to add another color that will complement our company colors

Note: will provide all text and pictures for the design....
I have all the content and pictures already set for the designer that will give full design details to make the design job easier for the designer. I will upload all content details once I select a designer for the job.

Target Market(s)

Professional. Brochure will be gear towards professionals in the apartment industry such as property managers

Industry/Entity Type

Entertainment

Other font styles liked:
• Open with the font

Colors

Designer to choose colors to be used in the design.

Requirements
Must have
• Professional brochure.
Should not have
• • Use too many font styles • Shrink text too small

```html
<!DOCTYPE html>
<html lang="en">
<head>
<meta charset="utf-8">
<title>Velora Entertainment – Tri-fold Brochure</title>
<link href="https://fonts.googleapis.com/css2?family=Montserrat:wght@500;600;700&display=swap" rel="stylesheet">
<style>
:root{
  --maroon:#9b1b1f;
  --maroon-deep:#7a1216;
  --white:#ffffff;
  --ink:#222222;
  --stage:#7d7d7d;
  --mist:#d9d9de;
  --grey-bar:#c9c9c9;
}
*{margin:0;padding:0;box-sizing:border-box}
html,body{width:1200px;height:2546px;overflow:hidden}
body{background:var(--stage);font-family:"Montserrat",Arial,sans-serif;color:var(--ink);position:relative}
.spread-frame{position:absolute;left:40px;width:1120px;height:863px;box-shadow:0 6px 18px rgba(0,0,0,.45);overflow:hidden}
.spread-frame.outer{top:370px}
.spread-frame.inner{top:1313px}
.spread{position:absolute;left:0;top:0;width:850px;height:655px;transform:scale(1.31765);transform-origin:0 0}
.spread svg.art{position:absolute;left:0;top:0;width:850px;height:655px}
.block{position:absolute}
.heading{font-weight:700;line-height:1.05}
.heading.caps{text-transform:uppercase;font-size:17px;color:var(--maroon)}
.heading.red{color:var(--maroon);font-size:17.5px}
.heading.light{color:var(--white);font-size:17.5px}
.with-icon{display:flex;align-items:center;gap:8px}
.icon{flex:0 0 26px;height:26px}
.copy{font-size:11.5px;font-weight:500;line-height:17.5px}
.copy p+p{margin-top:17px}
.copy.light{color:var(--white);font-weight:600}
.copy.loose{font-size:12px;line-height:21.5px}
.headline-white{color:var(--white);font-weight:700;text-transform:uppercase;text-align:center;line-height:1.12}
.web{position:absolute;top:612px;width:283px;text-align:center;font-size:12.5px;font-weight:600}
.web.light{color:var(--white)}
.web.red{color:var(--maroon)}
.brand-name{font-size:30px;font-weight:700;color:var(--maroon);letter-spacing:1px;line-height:1}
.brand-tag{font-size:10px;font-weight:500;color:var(--ink);margin-top:8px}
.checklist{list-style:none}
.checklist li{position:relative;padding-left:17px;color:var(--white);font-size:11.5px;font-weight:600;line-height:16.5px}
.checklist li::before{content:"";position:absolute;left:2px;top:4px;width:8px;height:4px;border-left:2px solid var(--white);border-bottom:2px solid var(--white);transform:rotate(-45deg)}
</style>
</head>
<body>

<!-- Outer spread -->
<div class="spread-frame outer">
  <div class="spread">
    <svg class="art" viewBox="0 0 850 655" aria-hidden="false">
      <defs>
        <linearGradient id="concertGlow" x1="0" y1="0" x2="1" y2="1">
          <stop offset="0" stop-color="#1c1f4a"/>
          <stop offset=".35" stop-color="#5d3b7a"/>
          <stop offset=".6" stop-color="#c8782a"/>
          <stop offset=".85" stop-color="#4a2a26"/>
          <stop offset="1" stop-color="#1a1a2a"/>
        </linearGradient>
      </defs>
      <rect width="850" height="655" fill="#ffffff"/>
      <rect x="283" y="0" width="284" height="655" fill="var(--maroon)"/>
      <path role="img" aria-label="Photo of a DJ in headphones facing a cheering concert crowd under stage lights"
            d="M0,0 H850 V372 C800,382 720,420 630,402 C520,380 440,260 340,185 C260,125 150,105 0,122 Z"
            fill="url(#concertGlow)"/>
      <path d="M0,545 C90,505 190,515 283,560 V655 H0 Z" fill="#e4e4e4"/>
      <path d="M760,655 L850,600 V655 Z" fill="#e0e0e0"/>
    </svg>

    <div class="block with-icon" style="left:22px;top:141px;width:250px">
      <svg class="icon" viewBox="0 0 26 26" aria-hidden="true"><circle cx="13" cy="7" r="4" fill="var(--ink)"/><circle cx="5" cy="10" r="3" fill="var(--ink)"/><circle cx="21" cy="10" r="3" fill="var(--ink)"/><path d="M7,24 L9,14 H17 L19,24 Z M1,22 L2,15 H7 L6,22 Z M25,22 L24,15 H19 L20,22 Z" fill="var(--ink)"/></svg>
      <div class="heading caps">Community<br>Event Experiences</div>
    </div>
    <div class="block copy loose" style="left:22px;top:193px;width:245px">
      <p>One of the ways we make it interactive, the virtual party guests have the opportunity to chat using the social platform chat system to talk with the LIVE DJ, other residents, family, friends or even our event sponsors</p>
      <p>At the same time, we have our inhouse show producers monitoring the chat room feed live to prevent any unwanted comments from appearing in the LIVE chat feed.</p>
    </div>

    <div class="block headline-white" style="left:283px;top:440px;width:284px;font-size:20px">Let’s curate<br>your next event<br>experience</div>
    <div class="web light" style="left:283px">www.veloraentertainment.com</div>

    <div class="block headline-white" style="left:590px;top:28px;width:240px;font-size:18.5px">More than entertainment. An experience your residents will remember.</div>
    <div class="block" style="left:600px;top:470px;width:230px;text-align:center">
      <div class="brand-name">VELORA</div>
      <div class="brand-name" style="font-size:14px;letter-spacing:3px;margin-top:4px">ENTERTAINMENT</div>
      <div class="brand-tag">DJ Services | Photo Booths | Event Lighting</div>
    </div>
    <div class="web red" style="left:567px">www.veloraentertainment.com</div>
  </div>
</div>

<!-- Inner spread -->
<div class="spread-frame inner">
  <div class="spread">
    <svg class="art" viewBox="0 0 850 655">
      <defs>
        <linearGradient id="mistPhoto" x1="0" y1="0" x2="1" y2="1">
          <stop offset="0" stop-color="#e6e6ea"/>
          <stop offset=".5" stop-color="#d4d2d8"/>
          <stop offset="1" stop-color="#e2dcdc"/>
        </linearGradient>
        <linearGradient id="darkStage" x1="0" y1="0" x2="0" y2="1">
          <stop offset="0" stop-color="#8e1a1e"/>
          <stop offset=".55" stop-color="#5a1418"/>
          <stop offset="1" stop-color="#2a1416"/>
        </linearGradient>
      </defs>
      <rect role="img" aria-label="Faded photo of a concert crowd under stage lights" width="850" height="655" fill="url(#mistPhoto)"/>
      <rect role="img" aria-label="Photo of a DJ at the decks facing a crowd" x="283" y="0" width="284" height="470" fill="url(#darkStage)"/>
      <path d="M0,362 C140,318 290,348 410,410 C520,468 660,478 850,438 V655 H0 Z" fill="var(--maroon)"/>
    </svg>

    <div class="block with-icon" style="left:18px;top:23px;width:255px">
      <svg class="icon" viewBox="0 0 26 26" aria-hidden="true"><circle cx="9" cy="14" r="7" fill="none" stroke="var(--ink)" stroke-width="2.5"/><circle cx="9" cy="14" r="2" fill="var(--ink)"/><path d="M15,6 L24,3 L22,12" fill="none" stroke="var(--ink)" stroke-width="2.5"/></svg>
      <div class="heading red">Interactive DJ +<br>Karaoke Experience</div>
    </div>
    <div class="block copy" style="left:20px;top:76px;width:245px">
      <p>Velora Entertainment can stage and create the ideal atmosphere for your corporate event. We have worked with small nonprofits to Fortune 500 companies in every industry across the country.</p>
      <p>Our DJ’s are trained to adapt and interact and our marketing specialists can help you brand your event. The Velora Entertainment team can make your corporate event one to remember</p>
    </div>

    <div class="block with-icon" style="left:18px;top:378px;width:255px">
      <svg class="icon" viewBox="0 0 26 26" aria-hidden="true"><circle cx="13" cy="13" r="3" fill="#fff"/><path d="M8,7 A8,8 0 0 0 8,19 M18,7 A8,8 0 0 1 18,19 M4,4 A13,13 0 0 0 4,22 M22,4 A13,13 0 0 1 22,22" fill="none" stroke="#fff" stroke-width="2"/></svg>
      <div class="heading light">Live Music<br>Experience</div>
    </div>
    <ul class="block checklist" style="left:20px;top:428px;width:255px">
      <li>Are you looking to wow your guests? Whether you are hosting a birthday party, wedding, grand opening, anniversary party or corporate event, live entertainment will add that extra touch to impress your guests. Velora Entertainment offers music for all occasions and performances like no other!</li>
      <li>Harpist</li>
      <li>Saxophone Player</li>
      <li>Singers</li>
    </ul>

    <div class="block with-icon" style="left:300px;top:23px;width:255px">
      <svg class="icon" viewBox="0 0 26 26" aria-hidden="true"><rect x="5" y="2" width="16" height="22" fill="none" stroke="#fff" stroke-width="2"/><rect x="9" y="6" width="8" height="6" fill="#fff"/><rect x="9" y="14" width="8" height="6" fill="#fff"/></svg>
      <div class="heading light">Photo Booth<br>Entertainment</div>
    </div>
    <div class="block copy light" style="left:301px;top:76px;width:250px">
      <p>If you are looking for something different, classy and elegant for your wedding, cocktail or dinner event, a live harpist offers the finest in unique entertainment for events of all sizes.</p>
    </div>
    <div class="block with-icon" style="left:300px;top:184px;width:255px">
      <svg class="icon" viewBox="0 0 26 26" aria-hidden="true"><rect x="3" y="5" width="20" height="18" rx="2" fill="#fff"/><rect x="7" y="2" width="3" height="6" fill="#fff"/><rect x="16" y="2" width="3" height="6" fill="#fff"/><path d="M13,11 L14.5,15 L18,15 L15,17 L16,21 L13,19 L10,21 L11,17 L8,15 L11.5,15 Z" fill="var(--maroon)"/></svg>
      <div class="heading light">Signature<br>Event Add-Ons</div>
    </div>
    <div class="block copy light" style="left:301px;top:237px;width:250px">
      <p>One of the ways we make it interactive, the virtual party guests have the opportunity to chat using the social platform chat system to talk with the LIVE DJ, other residents, family, friends or even our event sponsors</p>
    </div>

    <div class="block with-icon" style="left:584px;top:23px;width:255px">
      <svg class="icon" viewBox="0 0 26 26" aria-hidden="true"><path d="M2,12 A11,8 0 0 1 24,12 Z" fill="var(--ink)"/><rect x="4" y="13" width="18" height="10" fill="none" stroke="var(--ink)" stroke-width="2"/></svg>
      <div class="heading red">Ultimate Outdoor<br>Movie Experience</div>
    </div>
    <div class="block copy" style="left:585px;top:75px;width:245px">
      <p>Velora Entertainment offers the best in fully integrated digital solutions for entertainment. Our professional staff of experts will help you execute an event to remember, whether a corporate event, tradeshow, fashion show, wedding, private party, residential event or an award show.</p>
    </div>
    <div class="block with-icon" style="left:584px;top:258px;width:255px">
      <svg class="icon" viewBox="0 0 26 26" aria-hidden="true"><rect x="2" y="10" width="12" height="14" fill="var(--ink)"/><circle cx="8" cy="17" r="3" fill="#fff"/><circle cx="19" cy="7" r="5" fill="none" stroke="var(--ink)" stroke-width="2"/><rect x="16" y="14" width="7" height="10" fill="var(--ink)"/></svg>
      <div class="heading red">Event Production:<br>Audio, Visual &amp;<br>Lighting</div>
    </div>
    <div class="block copy" style="left:585px;top:327px;width:245px">
      <p>High-level events require more than great music. They require leadership, timing, production expertise, and the ability to control energy in any environment.</p>
    </div>

    <div class="web light" style="left:283px">www.veloraentertainment.com</div>
    <div class="web light" style="left:567px">www.veloraentertainment.com</div>
  </div>
</div>

</body>
</html>
```